Upmarket building and construction company needs signage

Our building company R Brent Construction, needs signage to put up on the side of our vehicle trailers and on site fencing. We are a building company that specialises in residential construction and carpentry .

I will attach our logo and some inspirational pics for site fencing as well as what our trailer looks like .
Other details i would like on the sign are our
( email) rbrentconstruction@mailbox-example.net
(mobile ) 0493 518 264
(website ) rbrentconstruction. example.net

Target Market(s)

Home owners looking for a reliable local builder who produces good quality work. I have attached some inspirational pics.

Industry/Entity Type

Building and Construction

Colors

Designer to choose colors to be used in the design.

Requirements
Must have
• Our logo, contact information
Nice to have
• We would like the design to have elements of being Elegant, Serious, Modern, Professional, Masculine, Conservative and Upmarket.

```html
<!DOCTYPE html>
<html lang="en">
<head>
<meta charset="utf-8">
<title>R Brent Construction – Site Fence Signage</title>
<link rel="stylesheet" href="https://fonts.googleapis.com/css2?family=Josefin+Sans:wght@300&family=Poppins:wght@400&display=swap">
<style>
  :root {
    --page: #ffffff;
    --panel: #727272;
    --ink: #ffffff;
  }
  html, body {
    margin: 0;
    padding: 0;
    width: 1200px;
    height: 900px;
    overflow: hidden;
    background: var(--page);
  }
  .canvas {
    position: relative;
    width: 1200px;
    height: 900px;
  }
  .banner {
    position: absolute;
    left: 41px;
    top: 310px;
    width: 1119px;
    height: 280px;
    background: var(--panel);
    overflow: hidden;
  }
  .rule {
    position: absolute;
    background: var(--ink);
  }
  .rule--divider { left: 559px; top: 0; width: 2px; height: 280px; }
  .rule--short { left: 583px; top: 0; width: 2px; height: 96px; }
  .rule--long { left: 601px; top: 38px; width: 2px; height: 242px; }

  .brand-name {
    position: absolute;
    left: 0;
    width: 559px;
    top: 112px;
    text-align: center;
    font-family: "Josefin Sans", sans-serif;
    font-weight: 300;
    color: var(--ink);
    font-size: 34px;
    letter-spacing: 3px;
    text-transform: uppercase;
    line-height: 1.25;
  }
  .contact {
    position: absolute;
    left: 625px;
    top: 44px;
    margin: 0;
    padding: 0;
    list-style: none;
    font-family: "Poppins", sans-serif;
    font-weight: 400;
    font-size: 11.5px;
    line-height: 20px;
    color: var(--ink);
  }
  .brand-name--small {
    position: absolute;
    right: 34px;
    top: 48px;
    font-family: "Josefin Sans", sans-serif;
    font-weight: 300;
    font-size: 9px;
    letter-spacing: 1px;
    color: var(--ink);
    text-transform: uppercase;
    text-align: center;
    line-height: 1.3;
  }
</style>
</head>
<body>
<main class="canvas">
  <section class="banner" aria-label="Site fence banner">
    <div class="brand-name">R Brent<br>Construction</div>
    <span class="rule rule--divider"></span>
    <span class="rule rule--short"></span>
    <span class="rule rule--long"></span>
    <ul class="contact">
      <li>rbrentconstruction@mailbox-example.net</li>
      <li>rbrentconstruction.example.net</li>
      <li>0493 518 264</li>
    </ul>
    <div class="brand-name--small">R Brent<br>Construction</div>
  </section>
</main>
</body>
</html>
```